Birchline Septic Solutions

Would like to see some single sided ones but would also like to see some double sided with one sided only being the logo. Owners name is Tom Waldrick. Phone number is 555-214-8830
Services are pumping, inspections, installs, and repairs

Contact Information for Business Card

555-241-8830 Tom Waldrick Cedarbrook, OH

```html
<!DOCTYPE html>
<html lang="en">
<head>
<meta charset="utf-8">
<title>Birchline Septic Solutions – Business Cards</title>
<link rel="stylesheet" href="https://fonts.googleapis.com/css2?family=Montserrat:wght@500;600;700;800&display=swap">
<style>
  :root {
    --bg: #1c1c1c;
    --card-black: #000000;
    --teal: #2dbdb9;
    --teal-dark: #229892;
    --swoosh: #ececec;
    --white: #ffffff;
  }
  * { margin: 0; padding: 0; box-sizing: border-box; }
  html, body {
    width: 1200px; height: 1015px; overflow: hidden;
    background: var(--bg);
    font-family: "Montserrat", sans-serif;
  }
  .stage { position: relative; width: 1200px; height: 1015px; }
  .card {
    position: absolute; width: 600px; height: 343px;
    background: var(--card-black); overflow: hidden;
    box-shadow: 0 18px 40px rgba(0,0,0,.55);
  }
  .card--front { left: 50px; top: 90px; }
  .card--back  { left: 550px; top: 570px; }
  .card__waves { position: absolute; inset: 0; width: 100%; height: 100%; }

  .brand {
    position: absolute; color: var(--white);
    font-weight: 700; display: flex; align-items: center; gap: 12px;
  }
  .brand__mark { width: 14px; height: 14px; background: var(--teal); flex: none; }
  .brand__text { display: flex; flex-direction: column; line-height: 1; }
  .brand__name { font-size: 46px; letter-spacing: -0.5px; }
  .brand__sub { font-size: 13px; letter-spacing: 5px; margin-top: 8px; }
  .card--front .brand { left: 150px; top: 95px; }
  .card--back .brand { right: 56px; top: 36px; }
  .card--back .brand__name { font-size: 40px; }
  .card--back .brand__sub { font-size: 11px; letter-spacing: 4px; }

  .services {
    position: absolute; right: 40px; top: 120px;
    list-style: none; text-align: right;
    color: var(--white); font-weight: 600; font-size: 14px;
    letter-spacing: .5px; line-height: 1.35;
  }
  .services li::after {
    content: ""; display: inline-block; width: 6px; height: 6px;
    background: var(--white); margin-left: 7px; vertical-align: middle;
  }

  .contact { position: absolute; left: 60px; bottom: 42px; color: var(--white); }
  .contact__name { font-weight: 800; font-size: 24px; letter-spacing: .5px; margin-bottom: 16px; }
  .contact__line { display: flex; align-items: center; gap: 10px; font-weight: 500; font-size: 17px; margin-top: 6px; }
  .contact__icon { width: 16px; height: 16px; flex: none; }
</style>
</head>
<body>
<main class="stage">

  <section class="card card--front" aria-label="Card front">
    <svg class="card__waves" viewBox="0 0 600 343" preserveAspectRatio="none" aria-hidden="true">
      <path d="M0,340 C180,310 300,260 380,170 C445,100 520,78 600,72 L600,343 L0,343 Z" fill="var(--teal)"/>
      <path d="M0,333 C180,303 300,252 380,162 C445,92 520,70 600,64 L600,72 C520,78 445,100 380,170 C300,260 180,310 0,340 Z" fill="var(--teal-dark)"/>
      <path d="M0,300 C150,318 290,285 355,205 C290,275 150,300 0,285 Z" fill="var(--swoosh)"/>
    </svg>
    <div class="brand">
      <span class="brand__text">
        <span class="brand__name">Birchline</span>
        <span class="brand__sub">SEPTIC SOLUTIONS</span>
      </span>
      <span class="brand__mark"></span>
    </div>
    <ul class="services">
      <li>PUMPING</li>
      <li>INSPECTIONS</li>
      <li>INSTALLS</li>
      <li>REPAIRS</li>
    </ul>
  </section>

  <section class="card card--back" aria-label="Card back">
    <svg class="card__waves" viewBox="0 0 600 343" preserveAspectRatio="none" aria-hidden="true">
      <path d="M0,235 C180,175 380,165 600,185 L600,343 L0,343 Z" fill="var(--teal)"/>
      <path d="M150,205 C300,172 450,168 600,182 L600,190 C450,178 300,180 150,205 Z" fill="var(--teal-dark)"/>
      <path d="M250,190 C380,165 500,160 600,168 L600,178 C500,172 380,176 250,190 Z" fill="var(--swoosh)"/>
      <path d="M440,160 C520,152 575,130 600,105 L600,165 C560,160 500,160 440,160 Z" fill="var(--teal)"/>
      <path d="M430,160 C515,145 565,122 588,98 L598,101 C572,130 520,152 430,160 Z" fill="var(--swoosh)"/>
    </svg>
    <div class="brand">
      <span class="brand__mark"></span>
      <span class="brand__text">
        <span class="brand__name">Birchline</span>
        <span class="brand__sub">SEPTIC SOLUTIONS</span>
      </span>
    </div>
    <div class="contact">
      <p class="contact__name">TOM WALDRICK</p>
      <p class="contact__line">
        <svg class="contact__icon" viewBox="0 0 24 24" aria-hidden="true"><path fill="var(--white)" d="M6.6 10.8a15.1 15.1 0 0 0 6.6 6.6l2.2-2.2a1 1 0 0 1 1-.25 11.4 11.4 0 0 0 3.6.57 1 1 0 0 1 1 1V20a1 1 0 0 1-1 1A17 17 0 0 1 3 4a1 1 0 0 1 1-1h3.5a1 1 0 0 1 1 1c0 1.25.2 2.45.57 3.6a1 1 0 0 1-.25 1Z"/></svg>
        555-214-8830
      </p>
      <p class="contact__line">
        <svg class="contact__icon" viewBox="0 0 24 24" aria-hidden="true"><path fill="var(--white)" d="M12 2a7 7 0 0 0-7 7c0 5.2 7 13 7 13s7-7.8 7-13a7 7 0 0 0-7-7Zm0 9.5A2.5 2.5 0 1 1 12 6.5a2.5 2.5 0 0 1 0 5Z"/></svg>
        Cedarbrook, OH
      </p>
    </div>
  </section>

</main>
</body>
</html>
```